Real Estate Team Needs Business Cards

Double sided - Team Member on Front, Team Leader on Back (back side will contain more details).
Colors to use:
Red = R: 233 G: 1 B: 2
Grey = R: 89 G: 89 B: 89
Black= R: 0 B: 0 B: 0
** MAIN FOCUS ** ( separate border, color, design, etc. to really stand out - whatever you think draws the most attention ) on both sides for "Sell for 1%‡" and "Buy & receive up to a 1% rebate‡". Must have fine print **
**Please make both sides stand out and look unique / different
Business card to have round corners (standard size 3.5" x 2").:
Document Trim Size
89 x 51 mm
1050 x 600 pixels
Full Bleed Size
92 x 54 mm
1085 x 635 pixels
Basic example provided. Please redesign as you see best. In your design - Please use the same picture on both sides. Name, address, phone number, email, etc. will be provided to the selected design. QR code on back side only if there is room (not important)

```html
<!DOCTYPE html>
<html lang="en">
<head>
<meta charset="utf-8">
<title>Northgate Realty – Business Card</title>
<link rel="stylesheet" href="https://fonts.googleapis.com/css2?family=Lato:wght@400;700&display=swap">
<style>
  :root {
    --brand-red: #e81e25;
    --text-grey: #8a8a8a;
    --stripe-grey: #8c8c8c;
    --page-bg: #dedede;
    --white: #ffffff;
  }
  * { box-sizing: border-box; margin: 0; padding: 0; }
  html, body {
    width: 1200px; height: 960px; overflow: hidden;
    background: var(--page-bg);
    font-family: "Lato", Arial, sans-serif;
  }
  .canvas { position: relative; width: 1200px; height: 960px; }
  .card {
    position: absolute; left: 281px; width: 655px; height: 374px;
    border-radius: 23px; overflow: hidden;
  }
  .card-front { top: 80px; background: var(--white); }
  .card-back { top: 506px; background: var(--brand-red); color: var(--white); }

  .front-panel { position: absolute; left: 0; top: 0; width: 171px; height: 100%; background: var(--brand-red); }
  .front-stripe { position: absolute; left: 171px; top: 0; width: 6px; height: 100%; background: var(--stripe-grey); }
  .portrait {
    position: absolute; left: 77px; top: 90px; width: 194px; height: 194px;
    border-radius: 50%; border: 4px solid var(--white);
    background: radial-gradient(circle at 50% 40%, #c9cbcc 0%, #b3b6b8 55%, #2c3f66 100%);
  }
  .details { position: absolute; left: 322px; top: 74px; }
  .agent-name { font-size: 28px; font-weight: 700; color: var(--brand-red); line-height: 1; letter-spacing: 0.2px; }
  .agent-title { font-size: 19px; color: var(--text-grey); margin-top: 4px; }
  .offer-headline { font-size: 26px; font-weight: 700; color: var(--brand-red); margin-top: 20px; line-height: 1.1; }
  .offer-sub { font-size: 17.5px; color: var(--text-grey); margin-top: 4px; }
  .contact-list { list-style: none; margin-top: 14px; }
  .contact-list li { display: flex; align-items: center; gap: 8px; font-size: 17px; color: var(--text-grey); height: 24px; }
  .contact-list svg { width: 13px; height: 13px; flex: none; fill: var(--brand-red); }

  .brand-name {
    position: absolute; left: 0; right: 0; top: 130px; text-align: center;
    font-size: 30px; font-weight: 700; letter-spacing: 1px; line-height: 1;
  }
  .brand-tagline {
    position: absolute; left: 186px; width: 340px; top: 177px;
    display: flex; align-items: center; gap: 8px;
    font-size: 9px; font-weight: 700; letter-spacing: 0.5px;
  }
  .brand-tagline::before, .brand-tagline::after { content: ""; flex: 1; height: 1px; background: var(--white); }
  .back-headline { position: absolute; left: 0; right: 0; top: 215px; text-align: center; font-size: 26px; font-weight: 700; }
  .back-sub { position: absolute; left: 0; right: 0; top: 245px; text-align: center; font-size: 18px; }
  .back-web {
    position: absolute; left: 0; right: 0; top: 308px;
    display: flex; align-items: center; gap: 8px; font-size: 18px;
  }
  .back-web::before, .back-web::after { content: ""; flex: 1; height: 1px; background: rgba(255,255,255,0.8); }
</style>
</head>
<body>
<main class="canvas">
  <section class="card card-front">
    <div class="front-panel"></div>
    <div class="front-stripe"></div>
    <div class="portrait" role="img" aria-label="Portrait photo of the agent in a suit"></div>
    <div class="details">
      <h1 class="agent-name">DANIEL MOREAU</h1>
      <p class="agent-title">Founder &amp; CEO</p>
      <p class="offer-headline">Sell for 1%*</p>
      <p class="offer-sub">Buy &amp; receive up to a 1% rebate*</p>
      <ul class="contact-list">
        <li><svg viewBox="0 0 14 14"><path d="M4 0h6a1 1 0 0 1 1 1v12a1 1 0 0 1-1 1H4a1 1 0 0 1-1-1V1a1 1 0 0 1 1-1zm.5 1.5v9h5v-9zM7 11.5a.8.8 0 1 0 0 1.6.8.8 0 0 0 0-1.6z"/></svg>(123) 123 1234</li>
        <li><svg viewBox="0 0 14 14"><path d="M3 1l2.5 2.5-1.2 1.6a8 8 0 0 0 4.6 4.6l1.6-1.2L13 11l-1.5 2A11 11 0 0 1 1 2.5z"/></svg>(123) 123 1234</li>
        <li><svg viewBox="0 0 14 14"><path d="M0 3h14v8H0zm1.2 1.2v.3L7 8l5.8-3.5v-.3zM1.2 6v3.8h11.6V6L7 9.5z"/></svg>info@northgaterealty.com</li>
        <li><svg viewBox="0 0 14 14"><path d="M7 0a7 7 0 1 0 0 14A7 7 0 0 0 7 0zm-5.6 6.3h2.4c.1-1.6.5-3 1.1-4A5.6 5.6 0 0 0 1.4 6.3zm0 1.4a5.6 5.6 0 0 0 3.5 4c-.6-1-1-2.4-1.1-4zm3.8 0c.1 2 .9 3.6 1.8 4 .9-.4 1.7-2 1.8-4zm3.6 0c-.1 1.6-.5 3-1.1 4a5.6 5.6 0 0 0 3.5-4zm2.4-1.4a5.6 5.6 0 0 0-3.5-4c.6 1 1 2.4 1.1 4zm-3.8 0c-.1-2-.9-3.6-1.8-4-.9.4-1.7 2-1.8 4z"/></svg>www.northgaterealty.com</li>
      </ul>
    </div>
  </section>

  <section class="card card-back">
    <p class="brand-name">NORTHGATE REALTY</p>
    <p class="brand-tagline">INC., BROKERAGE</p>
    <p class="back-headline">Sell for 1%*</p>
    <p class="back-sub">Buy &amp; receive up to a 1% rebate*</p>
    <p class="back-web">www.northgaterealty.com</p>
  </section>
</main>
</body>
</html>
```